Locksmith Business Cards

My father-in-law is in need of new business cards for his locksmith business and I need to impress him. Kindly help me out!

You can see the previous business card attached. It is a family run business in North Wales.

No individual names on the cards.

Key Things to Feature:
- The words "Prompt", "Local", "Reliable" (as you can see under the logo on the website)
- 24h Emergency Service
- Covering All of North Wales, the Wirral and Chester
- The color blue
- A key or a lock would be interesting (similar to the ones that come up when you google locksmith business card)

Optional (only if design includes bullet points, like the example below):
https://imgvaultexample.net/gallery/582214/77109/77109_9034417_582214_image.jpg
- Residential / Commercial / Automotive
- Alarms & Cameras
- Key Cutting & Safes

https://www.corswenydd-locksmiths.co.uk/

Industry/Entity Type

Locksmith

Contact Information for Business Card

01632 960 418
07700 900 562
corswenyddlocksmiths@mailbrook.example
Corswenydd Locksmiths, The Tan Barn, 7 Ferris Row, Llandudno LL99 4QX
www.corswenydd-locksmiths.co.uk

Requirements
Must have
• - The words "Prompt", "Local", "Reliable" (as you can see under the logo on the website)
• - 24h Emergency Service
• - Covering All of North Wales, the Wirral and Chester
Nice to have
• - A key or a lock would be interesting (similar to the ones that come up when you google locksmith business card)

```html
<!DOCTYPE html>
<html lang="en">
<head>
<meta charset="utf-8">
<title>Corswenydd Locksmiths – Business Cards</title>
<link href="https://fonts.googleapis.com/css2?family=Lato:wght@400&family=Oswald:wght@400;500;600&display=swap" rel="stylesheet">
<style>
  :root {
    --backdrop: #d8d8d5;
    --ink-blue: #353f8c;
    --band-blue: #4453a0;
    --bright-blue: #5062b4;
    --deep-blue: #262c66;
    --black: #0b0b0d;
    --white: #ffffff;
    --soft-grey: #c9c9c9;
    --paper: #f7f7f7;
  }
  * { margin: 0; padding: 0; box-sizing: border-box; }
  html, body { width: 1200px; height: 1176px; overflow: hidden; }
  body { background: var(--backdrop); position: relative; font-family: "Lato", sans-serif; }

  .card { position: absolute; left: 200px; width: 781px; overflow: hidden; box-shadow: 0 6px 18px rgba(0,0,0,.25); }

  /* Front */
  .card--front { top: 90px; height: 448px; background: linear-gradient(160deg, var(--white) 30%, #e6e6e6 100%); }
  .brand { position: absolute; display: flex; align-items: center; gap: 16px; }
  .brand__mark { background: var(--ink-blue); border-radius: 14px; flex: none; }
  .brand__name { font-family: "Oswald", sans-serif; font-weight: 500; color: var(--ink-blue); line-height: 1; text-transform: uppercase; }
  .card--front .brand { left: 230px; top: 64px; }
  .card--front .brand__mark { width: 74px; height: 98px; }
  .card--front .brand__name { font-size: 44px; }

  .front__rule { position: absolute; left: 0; right: 0; top: 229px; height: 8px; background: var(--band-blue); }
  .front__contact-band { position: absolute; left: 0; right: 0; top: 241px; height: 116px; background: var(--black); }
  .identity { position: absolute; right: 436px; top: 22px; text-align: right; }
  .identity__name { font-family: "Oswald", sans-serif; font-weight: 500; font-size: 40px; color: var(--soft-grey); line-height: 1.05; }
  .identity__title { font-size: 19px; color: var(--bright-blue); margin-top: 6px; }
  .divider { position: absolute; left: 370px; top: 12px; width: 2px; height: 92px; background: var(--band-blue); }
  .contact-list { position: absolute; left: 395px; top: 18px; list-style: none; }
  .contact-list li { display: flex; align-items: center; gap: 10px; font-size: 19px; color: #e3e3e3; height: 31px; white-space: nowrap; }
  .contact-list .contact-list__email { font-size: 16.5px; }
  .contact-list svg { width: 15px; height: 17px; fill: var(--band-blue); flex: none; }
  .address-band { position: absolute; left: 0; right: 0; top: 363px; height: 28px; background: var(--band-blue); color: #e4e6f2; font-size: 18.5px; line-height: 28px; padding-left: 57px; }

  /* Back */
  .card--back { top: 600px; height: 446px; background: radial-gradient(ellipse at 55% 40%, #1a1a1e 0%, var(--black) 70%); }
  .card--back .brand { left: 44px; top: 36px; }
  .card--back .brand__mark { width: 72px; height: 96px; background: var(--deep-blue); }
  .card--back .brand__name { font-size: 44px; color: #3b4796; }
  .tagline { position: absolute; left: 142px; top: 152px; font-family: "Oswald", sans-serif; font-weight: 600; font-size: 20px; color: var(--deep-blue); }
  .services { position: absolute; left: 40px; top: 214px; list-style: none; }
  .services li { position: relative; padding-left: 16px; font-size: 19px; color: #f0f0f0; height: 33px; }
  .services li::before { content: ""; position: absolute; left: 0; top: 10px; width: 7px; height: 7px; border-radius: 50%; background: var(--band-blue); }
  .web-band { position: absolute; left: 0; right: 0; top: 389px; height: 27px; }
  .web-band svg { position: absolute; inset: 0; }
  .web-band__url { position: absolute; left: 102px; top: 0; line-height: 27px; font-size: 18px; letter-spacing: 1.6px; color: #eef0fa; }
</style>
</head>
<body>

<section class="card card--front">
  <div class="brand">
    <div class="brand__mark"></div>
    <div class="brand__name">Corswenydd<br>Locksmiths</div>
  </div>
  <div class="front__rule"></div>
  <div class="front__contact-band">
    <div class="identity">
      <div class="identity__name">YOUR NAME</div>
      <div class="identity__title">JOB TITLE</div>
    </div>
    <div class="divider"></div>
    <ul class="contact-list">
      <li><svg viewBox="0 0 16 18"><path d="M3 1c1-.6 2 .2 2.6 1.4l1 2c.4.9 0 1.6-.7 2l-.8.5c.6 2 1.8 3.7 3.4 5l.8-.4c.8-.4 1.5-.2 2 .6l1.2 1.8c.6 1 .4 2-.5 2.6-1.5 1-3.5.8-5.5-1C3.4 12.7 1.6 9.2 1.3 5.6 1.1 3.5 1.8 1.8 3 1z"/></svg>01632 960 418</li>
      <li><svg viewBox="0 0 16 18"><path d="M4 0h8a1.5 1.5 0 0 1 1.5 1.5v15A1.5 1.5 0 0 1 12 18H4a1.5 1.5 0 0 1-1.5-1.5v-15A1.5 1.5 0 0 1 4 0zm0 2v12h8V2zm4 13a1 1 0 1 0 0 2 1 1 0 0 0 0-2z"/></svg>07700 900 562</li>
      <li class="contact-list__email"><svg viewBox="0 0 16 18"><path d="M0 4h16v11H0zm1.5 1.4v.4L8 10.2l6.5-4.4v-.4zM1.5 7.6v5.9h13V7.6L8 12z"/></svg>corswenyddlocksmiths@mailbrook.example</li>
    </ul>
  </div>
  <div class="address-band">Corswenydd Locksmiths, The Tan Barn, 7 Ferris Row, Llandudno LL99 4QX</div>
</section>

<section class="card card--back">
  <div class="brand">
    <div class="brand__mark"></div>
    <div class="brand__name">Corswenydd<br>Locksmiths</div>
  </div>
  <div class="tagline">Prompt. Local. Reliable</div>
  <ul class="services">
    <li>Residential / Commercial / Automotive</li>
    <li>Alarms &amp; Cameras</li>
    <li>Key Cutting &amp; Safes</li>
    <li>24h Emergency Service</li>
    <li>Covering All of North Wales, the Wirral and Chester</li>
  </ul>
  <div class="web-band">
    <svg width="781" height="27" viewBox="0 0 781 27" aria-hidden="true">
      <polygon points="0,0 496,0 485,27 0,27" fill="#4a5aa8"/>
      <polygon points="505,0 781,0 781,27 494,27" fill="#2c3372"/>
    </svg>
    <div class="web-band__url">www.corswenydd-locksmiths.co.uk</div>
  </div>
</section>

</body>
</html>
```